Manufacturing company needs new business card.

I need a unique Business Card that will truly stand out. Nothing too busy. Simple is good, right? Not looking for a standard design either. No cookie cutter layout. I am just looking for something interesting and a bit different. Does't have to completely off the wall crazy, just not your run of the mill business card. Clean and modern with a touch of industrial.

Target Market(s)

Air conditioning industry, Architects, builders.

Industry/Entity Type

Business

Contact Information for Business Card

Details to be included on card are:

Peter Vance
Managing Director

T: 1300 847 519
M: 0428 593 174
W: www.brenvaleworks.com.au
E: peter.vance@brenvaleworks.com.au
A: 58 Harwick Lane, Sydney NSW 2000

Font styles to use
Sans Serif

Colors
0355a3
848484
fbfbfb

Requirements
Must have
• Card design must be landscape.

```html
<!DOCTYPE html>
<html lang="en">
<head>
<meta charset="utf-8">
<title>Brenvale Works – Business Card</title>
<link href="https://fonts.googleapis.com/css2?family=Open+Sans:wght@400;600&display=swap" rel="stylesheet">
<style>
  :root {
    --brand-blue: #0355a3;
    --steel-grey: #848484;
    --paper: #fbfbfb;
    --backdrop: #e6e6e3;
    --name-grey: #6d6d6d;
  }
  * { margin: 0; padding: 0; box-sizing: border-box; }
  html, body {
    width: 1200px; height: 1200px; overflow: hidden;
    background: var(--backdrop);
    font-family: "Open Sans", sans-serif;
  }
  .canvas {
    position: relative; width: 1200px; height: 1200px;
  }
  .card {
    position: absolute; left: 160px;
    width: 880px; height: 503px;
    background: var(--paper);
    overflow: hidden;
    box-shadow: 0 6px 18px rgba(0,0,0,0.12);
  }
  .card--contact { top: 70px; }
  .card--brand { top: 627px; }

  /* brand lockup */
  .brand { position: absolute; display: flex; align-items: center; gap: 22px; }
  .brand__mark { background: var(--brand-blue); flex: none; }
  .brand__name {
    color: var(--brand-blue); font-weight: 600; letter-spacing: -0.5px; white-space: nowrap;
  }
  .brand__rule { position: absolute; height: 3px; background: var(--steel-grey); }

  .card--contact .brand { left: 110px; top: 96px; }
  .card--contact .brand__mark { width: 62px; height: 62px; }
  .card--contact .brand__name { font-size: 52px; }
  .card--contact .brand__rule { left: 194px; top: 184px; width: 300px; }

  .divider { position: absolute; left: 440px; top: 230px; }

  .contact-list {
    position: absolute; left: 560px; top: 226px;
    list-style: none; color: var(--brand-blue); font-size: 19px; line-height: 1.3;
  }
  .contact-list li { display: flex; align-items: flex-start; gap: 12px; margin-bottom: 14px; }
  .contact-list svg { flex: none; margin-top: 2px; }

  .person { position: absolute; left: 100px; top: 322px; }
  .person__name { font-size: 42px; color: var(--name-grey); font-weight: 400; line-height: 1.1; }
  .person__role { font-size: 19px; color: var(--brand-blue); margin-left: 28px; }

  .email {
    position: absolute; left: 310px; top: 432px;
    display: flex; align-items: center; gap: 12px;
    color: var(--brand-blue); font-size: 20px;
  }
  .edge-band {
    position: absolute; right: 0; bottom: 0; width: 460px; height: 44px;
    background: var(--steel-grey);
    clip-path: polygon(30% 70%, 100% 0, 100% 100%, 0 100%);
  }
  .corner-accent {
    position: absolute; left: 0; bottom: 0; width: 60px; height: 70px;
    background: var(--brand-blue);
    clip-path: polygon(0 0, 100% 100%, 0 100%);
  }

  .card--brand .brand { left: 110px; top: 150px; }
  .card--brand .brand__mark { width: 90px; height: 90px; }
  .card--brand .brand__name { font-size: 66px; }
  .card--brand .brand__rule { left: 224px; top: 268px; width: 360px; }

  .web-rule { position: absolute; left: 0; right: 0; top: 385px; height: 5px; background: var(--brand-blue); }
  .web-band {
    position: absolute; left: 0; right: 0; top: 402px; height: 62px;
    background: var(--brand-blue);
    display: flex; align-items: center; justify-content: center; gap: 12px;
    color: #fff; font-size: 21px;
  }
</style>
</head>
<body>
<main class="canvas">

  <section class="card card--contact" aria-label="Business card, contact side">
    <div class="brand">
      <span class="brand__mark"></span>
      <span class="brand__name">Brenvale Works</span>
    </div>
    <span class="brand__rule"></span>

    <svg class="divider" width="90" height="150" viewBox="0 0 90 150" aria-hidden="true">
      <g stroke="#0355a3" stroke-width="2.5" fill="none">
        <line x1="10" y1="0" x2="30" y2="110"/>
        <line x1="28" y1="10" x2="50" y2="130"/>
        <line x1="48" y1="20" x2="72" y2="150"/>
      </g>
    </svg>

    <ul class="contact-list">
      <li>
        <svg width="20" height="24" viewBox="0 0 20 24" aria-hidden="true"><path d="M10 1a7 7 0 0 0-7 7c0 5 7 13 7 13s7-8 7-13a7 7 0 0 0-7-7z" fill="none" stroke="#848484" stroke-width="2"/><circle cx="10" cy="8" r="2.5" fill="#848484"/></svg>
        <span>58 Harwick Lane,<br>Sydney NSW 2000</span>
      </li>
      <li>
        <svg width="22" height="20" viewBox="0 0 22 20" aria-hidden="true"><path d="M2 7c0-3 18-3 18 0v2h-5V7H7v2H2z" fill="#848484"/><rect x="4" y="10" width="14" height="9" rx="2" fill="none" stroke="#848484" stroke-width="2"/></svg>
        <span>1300 847 519</span>
      </li>
      <li>
        <svg width="20" height="24" viewBox="0 0 20 24" aria-hidden="true"><rect x="4" y="1" width="12" height="21" rx="2" fill="none" stroke="#848484" stroke-width="2"/><line x1="8" y1="18" x2="12" y2="18" stroke="#848484" stroke-width="2"/></svg>
        <span>0428 593 174</span>
      </li>
    </ul>

    <div class="person">
      <p class="person__name">Peter Vance</p>
      <p class="person__role">Managing Director</p>
    </div>

    <p class="email">
      <svg width="24" height="18" viewBox="0 0 24 18" aria-hidden="true"><rect x="1" y="1" width="22" height="16" fill="none" stroke="#848484" stroke-width="2"/><path d="M1 1l11 9 11-9" fill="none" stroke="#848484" stroke-width="2"/></svg>
      peter.vance@brenvaleworks.com.au
    </p>

    <span class="corner-accent"></span>
    <span class="edge-band"></span>
  </section>

  <section class="card card--brand" aria-label="Business card, brand side">
    <div class="brand">
      <span class="brand__mark"></span>
      <span class="brand__name">Brenvale Works</span>
    </div>
    <span class="brand__rule"></span>

    <span class="web-rule"></span>
    <p class="web-band">
      <svg width="22" height="22" viewBox="0 0 22 22" aria-hidden="true"><g fill="none" stroke="#fff" stroke-width="1.5"><circle cx="11" cy="11" r="9.5"/><ellipse cx="11" cy="11" rx="4.5" ry="9.5"/><line x1="1.5" y1="11" x2="20.5" y2="11"/><line x1="3" y1="6" x2="19" y2="6"/><line x1="3" y1="16" x2="19" y2="16"/></g></svg>
      www.brenvaleworks.com.au
    </p>
  </section>

</main>
</body>
</html>
```